Website Header for new website

We need a header/banner design for our revised website. Here is the link to our existing website lorimentaskel.me and to our new website in process seasonbrightway.us
Area of expertise is older adults, baby boomers and caregivers
This is an individual, professional website for a Speaker, Keynoter, Author, Brocaster

Target Market(s)

Event planners, broadcasters, publishers

Font styles to use
Serif

```html
<!DOCTYPE html>
<html lang="en">
<head>
<meta charset="utf-8">
<title>Lori Mentaskel — Speaker, Author, Broadcaster</title>
<link href="https://fonts.googleapis.com/css2?family=Bitter:wght@700&family=Alegreya:wght@400&family=Libre+Baskerville:wght@400&family=Roboto:wght@400;500;700&display=swap" rel="stylesheet">
<style>
:root{
  --ink:#111;
  --page:#efefef;
  --white:#fff;
  --card:#3b36ff;
  --navy:#0b2a6e;
  --blue:#1f6fd6;
  --sky:#3a9cf0;
  --rule:#3347d6;
  --light:#dfe9fb;
}
*{margin:0;padding:0;box-sizing:border-box}
html,body{width:1200px;height:547px;overflow:hidden;background:var(--page);font-family:'Roboto',sans-serif;color:var(--ink)}
.canvas{position:relative;width:1200px;height:547px;overflow:hidden}
.topbar{position:absolute;left:0;top:0;width:1200px;height:61px;background:var(--white);z-index:3}
.brand{position:absolute;left:21px;top:11px;width:176px;height:35px;border:2px solid #222;display:flex;align-items:center;justify-content:center;font-family:'Libre Baskerville',serif;font-size:13.5px;white-space:nowrap;overflow:hidden;letter-spacing:0}
.nav{position:absolute;left:276px;top:19px;display:flex;font-size:11px;white-space:nowrap}
.nav a{color:#222;text-decoration:none;margin-right:35px}
.nav a.has-menu::after{content:"";display:inline-block;width:4px;height:4px;border-right:1px solid #222;border-bottom:1px solid #222;transform:rotate(45deg);margin:0 0 2px 4px}
.hero{position:absolute;left:0;top:61px;width:1200px;height:264px;background:var(--white)}
.hero svg{position:absolute;left:0;top:0}
.portrait{position:absolute;left:100px;top:10px;width:230px;height:254px;border-radius:110px 110px 0 0;background:linear-gradient(180deg,#d8b48a 0%,#e07a3c 45%,#c9451a 100%)}
.name-box{position:absolute;left:356px;top:41px;width:297px;height:52px;border:2px solid var(--light);display:flex;align-items:center;justify-content:center;font-family:'Bitter',serif;font-weight:700;font-size:36px;color:var(--white);white-space:nowrap}
.hero-rule{position:absolute;left:356px;top:109px;width:844px;height:1px;background:var(--light)}
.roles{position:absolute;top:122px;font-family:'Alegreya',serif;font-size:21px;line-height:31px;color:var(--light);white-space:nowrap}
.roles.left{left:356px}.roles.right{left:600px}
.featured{position:absolute;left:806px;top:15px;width:78px;height:15px;border:1.5px solid var(--white);color:var(--white);font:700 8px 'Roboto',sans-serif;letter-spacing:.8px;display:flex;align-items:center;justify-content:center}
.badges{position:absolute;left:806px;top:39px;display:flex;gap:11px}
.badge{width:53px;height:53px;border-radius:8px;background:var(--white)}
.card{position:absolute;top:295px;height:135px;background:var(--card);color:var(--white);text-align:center}
.card h2{font-weight:500;font-size:16px;margin-top:18px;white-space:nowrap}
.card-podcast{left:184px;width:267px}
.card-speaker{left:461px;width:266px;height:133px}
.card-social{left:737px;width:266px;height:130px}
.thumb{position:absolute}
.card-podcast .thumb{left:16px;top:46px;width:59px;height:59px;background:linear-gradient(160deg,#3a2a1e,#7a5c44)}
.card-speaker .thumb{left:16px;top:43px;width:61px;height:74px;background:linear-gradient(180deg,#24314f,#6b7080)}
.excerpt{position:absolute;left:82px;top:46px;width:182px;font-size:11px;line-height:17.5px;color:#dcdcff}
.excerpt b{color:var(--white);font-weight:400}
.card-podcast .divider{position:absolute;left:16px;right:16px;top:119px;height:1px;background:rgba(255,255,255,.12)}
.card-speaker .link{position:absolute;left:80px;top:46px;width:170px;font-size:11px;text-align:center}
.social{display:flex;justify-content:center;gap:12px;margin-top:12px;font-size:11px;font-weight:700}
.social span::before{content:"";display:inline-block;width:6px;height:6px;border-radius:50%;background:var(--white);margin-right:4px;vertical-align:1px}
.email{margin-top:23px;font-size:11px;font-weight:500}
.panel{position:absolute;left:184px;top:454px;width:821px;height:120px;background:var(--white)}
.panel-rule{position:absolute;left:362px;top:27px;width:98px;height:2px;background:var(--rule)}
.panel h3{position:absolute;left:55px;top:62px;font-size:18px;font-weight:700}
.panel-image{position:absolute;left:427px;top:61px;width:339px;height:60px;background:linear-gradient(180deg,#f1ece8,#e6ddd6)}
</style>
</head>
<body>
<div class="canvas">
  <header class="topbar">
    <div class="brand">LORI MENTASKEL</div>
    <nav class="nav">
      <a>Home</a><a>Meet Lori</a><a class="has-menu">Speaker/Spokesperson</a><a>Blog</a><a>Podcast</a><a>Books</a><a>Work with Lori</a><a>Contact</a><a>Press</a>
    </nav>
  </header>

  <section class="hero">
    <svg width="1200" height="264" viewBox="0 0 1200 264" aria-hidden="true">
      <defs>
        <linearGradient id="heroBlue" x1="0" y1="0" x2="1" y2="0.3">
          <stop offset="0" stop-color="#0a2466"/>
          <stop offset="0.45" stop-color="#1a56b8"/>
          <stop offset="1" stop-color="#2f8fea"/>
        </linearGradient>
        <filter id="soft"><feGaussianBlur stdDeviation="6"/></filter>
      </defs>
      <polygon points="6,0 150,0 38,264 0,264" fill="#f2f2f2" filter="url(#soft)"/>
      <polygon points="150,0 1200,0 1200,170 1150,264 38,264" fill="url(#heroBlue)"/>
      <polygon points="150,0 330,0 220,264 38,264" fill="#0a2466" opacity=".5"/>
    </svg>
    <div class="portrait" role="img" aria-label="Portrait photo of Lori Mentaskel in an orange jacket"></div>
    <div class="name-box">Lori Mentaskel</div>
    <div class="hero-rule"></div>
    <div class="roles left">Dynamic Keynoter<br>Motivating Speaker<br>Influential Broadcaster</div>
    <div class="roles right">Prolific Author<br>Enteraining Blogger<br>Effective Trainer</div>
    <div class="featured">FEATURED ON</div>
    <div class="badges">
      <div class="badge"></div><div class="badge"></div><div class="badge"></div>
      <div class="badge"></div><div class="badge"></div><div class="badge"></div>
    </div>
  </section>

  <article class="card card-podcast">
    <h2>Our Latest Podcast</h2>
    <div class="thumb" role="img" aria-label="Headshot of podcast guest"></div>
    <p class="excerpt"><b>Podcast Guest: Dana Corwell, HALO</b> Season Brightway Radio, July 26– Guest: Dana Corwell, ...<b>Click Here</b></p>
    <div class="divider"></div>
  </article>

  <article class="card card-speaker">
    <h2>Speaker/Spokesperson</h2>
    <div class="thumb" role="img" aria-label="Photo of Lori speaking at a podium"></div>
    <p class="link">Topics &amp; Testimonials</p>
  </article>

  <article class="card card-social">
    <h2>Follow Us on Social Media</h2>
    <div class="social"><span>Linkwise</span><span>Chirper</span><span>Friendbook</span></div>
    <p class="email">hello@lorimentaskel.me</p>
  </article>

  <section class="panel">
    <div class="panel-rule"></div>
    <h3>Influence &amp; Entertain</h3>
    <div class="panel-image" role="img" aria-label="Feature photo for the Influence and Entertain section"></div>
  </section>
</div>
</body>
</html>
```